HearthBay business card and stationary design

We are looking for a simple yet elegant design for our mortgage company business card and stationary.

The card should include:
Name (Doug Warley)
Title (CEO)
Phone Number (614-382-9047)
Address (48 Birchwood Terrace, Suite 315, Marlow, NJ 08214)
Email (email@hearthbay.example)
"NMLS" i.e. (NMLS 61947)
"Company NMLS" (Company NMLS 492716)

Contact Information for Business Card

See above

```html
<!DOCTYPE html>
<html lang="en">
<head>
<meta charset="utf-8">
<title>HearthBay Business Card</title>
<link href="https://fonts.googleapis.com/css2?family=Montserrat:wght@400;500;600;700&display=swap" rel="stylesheet">
<style>
  :root {
    --navy: #1b2633;
    --blue: #27a7e1;
    --ink: #1e2430;
    --paper: #ffffff;
    --backdrop: #d9d9d7;
    --rule: #3a3f47;
  }
  * { box-sizing: border-box; margin: 0; padding: 0; }
  html, body {
    width: 1200px; height: 801px; overflow: hidden;
    background: var(--backdrop);
    font-family: "Montserrat", sans-serif;
    color: var(--ink);
  }
  .sheet {
    position: relative; width: 1200px; height: 801px;
  }
  .card {
    position: absolute; top: 252px;
    width: 520px; height: 297px;
    border-bottom: 6px solid var(--blue);
    box-shadow: 0 10px 24px rgba(0,0,0,.18);
  }
  .card-front { left: 50px; background: var(--paper); }
  .card-back { left: 630px; background: var(--navy); display: flex; align-items: center; justify-content: center; }

  .wordmark {
    position: absolute; top: 46px; right: 36px;
    font-weight: 600; font-size: 40px; letter-spacing: -0.5px;
    color: var(--navy);
  }
  .card-back .wordmark {
    position: static; font-size: 68px; color: var(--paper);
  }

  .person { position: absolute; left: 34px; top: 150px; }
  .person-name {
    font-weight: 700; font-size: 24px; letter-spacing: 0.5px; line-height: 1;
    color: var(--navy);
  }
  .person-name .surname { color: var(--blue); }
  .person-title { font-weight: 500; font-size: 12px; margin-top: 4px; color: var(--navy); }

  .divider {
    position: absolute; left: 34px; right: 34px; top: 196px;
    height: 1px; background: var(--rule);
  }

  .contacts { position: absolute; left: 34px; top: 208px; list-style: none; font-size: 12px; line-height: 17px; }
  .contacts .license { color: var(--blue); font-weight: 500; }
  .contacts li { display: flex; align-items: center; gap: 6px; }
  .contacts svg { width: 10px; height: 10px; fill: var(--blue); flex: none; }

  .office {
    position: absolute; right: 34px; top: 214px;
    text-align: right; font-size: 12px; line-height: 18px;
  }
  .office .license { color: var(--blue); font-weight: 500; }
</style>
</head>
<body>
<main class="sheet">
  <section class="card card-front" aria-label="Business card front">
    <div class="wordmark">HearthBay</div>

    <div class="person">
      <div class="person-name">DOUG <span class="surname">WARLEY</span></div>
      <div class="person-title">CEO</div>
    </div>

    <div class="divider"></div>

    <ul class="contacts">
      <li class="license">NMLS 61947</li>
      <li>
        <svg viewBox="0 0 10 10" aria-hidden="true"><path d="M2 0.5 L3.6 2.6 L2.7 3.6 Q3.6 5.8 6.3 7.2 L7.3 6.3 L9.5 7.9 L8.3 9.5 Q1 8 0.5 1.7 Z"/></svg>
        614-382-9047
      </li>
      <li>
        <svg viewBox="0 0 10 10" aria-hidden="true"><path d="M0 2 H10 V8.5 H0 Z M0.6 2.4 L5 5.6 L9.4 2.4" stroke="#fff" stroke-width="0.8"/></svg>
        email@hearthbay.example
      </li>
      <li>
        <svg viewBox="0 0 10 10" aria-hidden="true"><circle cx="5" cy="5" r="4.6"/><path d="M0.5 5 H9.5 M5 0.5 Q2.4 5 5 9.5 M5 0.5 Q7.6 5 5 9.5" stroke="#fff" stroke-width="0.7" fill="none"/></svg>
        www.hearthbay.example
      </li>
    </ul>

    <address class="office" style="font-style: normal;">
      48 Birchwood Terrace, Suite 315<br>
      Marlow, NJ 08214<br>
      <span class="license">Company NMLS 492716</span>
    </address>
  </section>

  <section class="card card-back" aria-label="Business card back">
    <div class="wordmark">HearthBay</div>
  </section>
</main>
</body>
</html>
```